Need simple and modern looking business card with all my information on one side and logo on the other side
Info :
Company name - VELMAR CONSTRUCTION LLC
Company addres- 418 harbor 87th. Dunmoor park ny 10352
Email- velmarllc@tridomail.Com
Company phone number 555-318-6094
Cell number- 555-742-0583
Web site - velmarllc.Com
My name Gerald tomasino

Target Market(s)

Construction , home improvement, remodeling

Industry/Entity Type

Construction

Contact Information for Business Card

It has to be moder but at the same time simple

Font styles to use
Sans Serif

Colors
0255a3
ffffff
000000
f78f20
b1b1b1
9d9d9d
1b1b1b
33a6d7
ec1f27

Requirements
Must have
• My logo on one side maybe with a some kind of background on the other side all my information
Nice to have
• Some kind of background pictures provided by you .PLEASE HAVE ACCOUNT WITH PIXELVAULT WILL NOT PAY ANY EXTRA FEES .
Should not have
• Any kind of hamer, nails,screws, helmets itp. Please do not copy the other designs come up with something new.

```html
<!DOCTYPE html>
<html lang="en">
<head>
<meta charset="utf-8">
<title>Velmar Construction LLC – Business Card</title>
<link rel="stylesheet" href="https://fonts.googleapis.com/css2?family=Noto+Sans:wght@400;600&display=swap">
<style>
  :root {
    --canvas-bg: #e4e4e4;
    --card-white: #ffffff;
    --ink: #1b1b1b;
    --ink-soft: #333333;
    --accent-blue: #3d6fc6;
    --brand-blue: #0255a3;
    --brand-red: #ec1f27;
    --brand-orange: #f78f20;
    --rule-orange: #f7c9a0;
    --band-grey: #4a4a4a;
  }
  * { box-sizing: border-box; margin: 0; padding: 0; }
  html, body {
    width: 1200px; height: 1200px; overflow: hidden;
    background: var(--canvas-bg);
    font-family: "Noto Sans", "DejaVu Sans", sans-serif;
  }
  .canvas { position: relative; width: 1200px; height: 1200px; }

  .card {
    position: absolute; left: 164px;
    width: 872px; height: 490px;
    background: var(--card-white);
    overflow: hidden;
  }
  .card--front { top: 80px; }
  .card--back { top: 630px; }

  /* Brand name block */
  .brand {
    position: absolute;
    display: flex; align-items: center; gap: 14px;
    color: var(--ink);
    font-weight: 600;
    letter-spacing: 1px;
    white-space: nowrap;
  }
  .brand__square {
    width: 26px; height: 26px;
    background: var(--brand-orange);
    flex: none;
  }
  .card--front .brand { right: 42px; top: 118px; font-size: 28px; }
  .card--back .brand {
    left: 50%; top: 214px; transform: translateX(-50%);
    font-size: 32px;
  }

  /* Front details */
  .holder-name {
    position: absolute; left: 38px; top: 244px;
    font-size: 33px; font-weight: 400;
    color: var(--accent-blue);
  }
  .divider {
    position: absolute; left: 38px; right: 42px; top: 302px;
    height: 2px; background: var(--rule-orange);
  }
  .contact-list {
    position: absolute; left: 38px; top: 318px;
    font-size: 25px; line-height: 31px;
    display: grid; grid-template-columns: 94px auto;
  }
  .contact-list dt { color: var(--accent-blue); }
  .contact-list dd { color: var(--ink-soft); }
  .company-address {
    position: absolute; right: 42px; top: 348px;
    text-align: right;
    font-size: 25px; line-height: 31px;
    color: var(--ink-soft);
    font-style: normal;
  }
  .color-bar {
    position: absolute; left: 0; right: 0; bottom: 0; height: 22px;
    display: flex;
  }
  .color-bar__blue { width: 612px; background: var(--accent-blue); }
  .color-bar__red { width: 140px; background: var(--brand-red); }
  .color-bar__orange { flex: 1; background: var(--brand-orange); }

  /* Back */
  .band {
    position: absolute; left: 0; right: 0;
    background: var(--band-grey);
  }
  .band--top { top: 0; height: 120px; }
  .band--bottom { bottom: 0; height: 120px; }
  .back-url {
    position: absolute; left: 0; right: 0; bottom: 26px;
    text-align: center;
    font-size: 26px; color: var(--card-white);
    letter-spacing: 0.5px;
  }
</style>
</head>
<body>
<main class="canvas">

  <section class="card card--front" aria-label="Business card front">
    <div class="brand">
      <span class="brand__square"></span>
      <span class="brand__name">VELMAR CONSTRUCTION LLC</span>
    </div>

    <h1 class="holder-name">Gerald tomasino</h1>
    <div class="divider"></div>

    <dl class="contact-list">
      <dt>Email</dt><dd>velmarllc@tridomail.Com</dd>
      <dt>Phone</dt><dd>555-318-6094</dd>
      <dt>Cell</dt><dd>555-742-0583</dd>
      <dt>Web</dt><dd>velmarllc.Com</dd>
    </dl>

    <address class="company-address">
      VELMAR CONSTRUCTION LLC<br>
      418 harbor 87th.<br>
      Dunmoor Park NY 10352
    </address>

    <div class="color-bar">
      <span class="color-bar__blue"></span>
      <span class="color-bar__red"></span>
      <span class="color-bar__orange"></span>
    </div>
  </section>

  <section class="card card--back" aria-label="Business card back">
    <div class="band band--top"></div>
    <div class="brand">
      <span class="brand__square"></span>
      <span class="brand__name">VELMAR CONSTRUCTION LLC</span>
    </div>
    <div class="band band--bottom"></div>
    <p class="back-url">velmarllc.com</p>
  </section>

</main>
</body>
</html>
```